2 Page Brochure - Commercial Roofing Company

We are looking for a double sided brochure, full color, for our commercial roofing company that tells customers a little bit about the company, what we do, and shows a few pictures.
The brochure would need to have our logo and color scheme that coordinates with that logo.
I have uploaded our logo, some ideas I had, and then the idea list also has our website on there if you'd like to take a look around there for some more ideas.
I have also uploaded some photos we'd like to use.
Page size should be 8.5" x 11".
Target Market(s)
Commercial Property Owners
Other font styles liked:
- Match logo font ideally so it's cohesive, but whatever looks best
Look and feel

```html
<!DOCTYPE html>
<html lang="en">
<head>
<meta charset="utf-8">
<title>Summitcrest Roofing – Brochure</title>
<link href="https://fonts.googleapis.com/css2?family=Poppins:wght@400;500;600;700&display=swap" rel="stylesheet">
<style>
  :root{
    --orange:#e85a1e;
    --ink:#161a22;
    --white:#ffffff;
    --stage:#b3b3b3;
    --paper:#eeeeee;
  }
  *{box-sizing:border-box;margin:0;padding:0}
  html,body{width:751px;height:1200px;overflow:hidden}
  body{background:var(--stage);font-family:'Poppins',sans-serif;color:var(--ink);position:relative}
  .page{position:absolute;left:30px;width:694px;overflow:hidden;box-shadow:1px 2px 4px rgba(0,0,0,.35)}
  .front{top:48px;height:536px;background:var(--paper)}
  .back{top:625px;height:535px;background:var(--ink);color:var(--white)}
  .abs{position:absolute}
  svg.art{position:absolute;left:0;top:0}
  .orange{color:var(--orange)}

  /* front */
  .contact{left:48px;width:240px;top:30px;text-align:center}
  .contact-icons{display:flex;justify-content:center;gap:6px;margin-bottom:6px}
  .contact-icons span{width:19px;height:19px;border:1.3px solid var(--ink);border-radius:50%;display:flex;align-items:center;justify-content:center}
  .phone{font-size:21px;font-weight:700;color:var(--orange);line-height:26px;letter-spacing:.5px}
  .web{font-size:12px;font-weight:600;margin-top:2px}
  .address{font-size:12px;font-weight:500;line-height:15px;margin-top:6px}
  .rule{width:38px;height:2px;background:var(--orange);margin:9px auto 0}
  .brand-top{left:400px;width:234px;top:22px;text-align:center;font-weight:700;line-height:1;color:var(--ink)}
  .brand-top .l1{font-size:27px;letter-spacing:.5px}
  .brand-top .l2{font-size:27px;margin-top:6px}
  .band{left:0;top:416px;width:694px;height:120px;background:var(--ink)}
  .brand-band{left:79px;width:180px;top:14px;text-align:center;color:var(--white);font-weight:700;line-height:1}
  .brand-band .l1{font-size:21px}
  .brand-band .l2{font-size:21px;margin-top:4px}
  .roc{left:79px;top:81px;width:180px;height:18px;border:1.2px solid var(--orange);text-align:center;font-size:11px;font-weight:700;line-height:16px;color:var(--white)}
  .tagline{left:360px;width:314px;top:18px;text-align:center;color:var(--white);font-weight:600;font-size:21px;line-height:25px}
  .web-bar{left:390px;top:82px;width:254px;height:16px;background:var(--orange);text-align:center;font-size:10px;font-weight:600;letter-spacing:2.2px;line-height:16px;color:var(--ink)}

  /* back */
  .h2{font-size:17px;font-weight:700;line-height:21px}
  .underline{height:2px;width:38px;background:var(--orange)}
  .about{left:20px;width:305px;top:88px;text-align:right}
  .about p{font-size:8.4px;line-height:10.5px;margin-bottom:10px}
  .about .underline{margin:4px 0 11px auto}
  .services-title{left:68px;width:200px;top:345px;text-align:center}
  .services-title .underline{margin:4px auto 0}
  .service{width:110px;text-align:center;font-size:8.4px;font-weight:500;line-height:10.5px}
  .service .ico{width:30px;height:30px;border:1.2px solid var(--orange);border-radius:50%;margin:0 auto 8px;display:flex;align-items:center;justify-content:center}
  .install{left:367px;top:88px;width:300px}
  .install .underline{margin-top:5px}
  .products{left:367px;top:171px;width:310px;font-size:8.4px;font-weight:500;line-height:18.5px}
  .products .sep{display:inline-block;width:1px;height:11px;background:var(--orange);margin:0 4px;vertical-align:-2px}
  .certified{left:367px;width:304px;top:245px;text-align:center}
  .certified .underline{margin:5px auto 0}
  .badge{position:absolute;width:75px;height:73px;background:var(--white)}
  .badge i{position:absolute;left:22px;top:22px;width:31px;height:29px;background:#dcdcdc;border-radius:3px}
  .more{left:367px;width:304px;top:467px;text-align:center;font-size:9px;letter-spacing:2.6px;font-weight:500}
  .serving{left:367px;top:491px;width:304px;height:23px;border:1px solid var(--orange);display:flex;font-size:10.5px;font-weight:700}
  .serving .a{width:68px;text-align:center;line-height:21px;color:var(--orange)}
  .serving .b{flex:1;background:var(--orange);text-align:center;line-height:21px;color:var(--white)}
</style>
</head>
<body>

<section class="page front">
  <svg class="art" width="694" height="416" viewBox="0 0 694 416">
    <defs>
      <linearGradient id="bgPaper" x1="0" y1="0" x2="1" y2="1">
        <stop offset="0" stop-color="#e6e6e6"/><stop offset=".5" stop-color="#f7f7f7"/><stop offset="1" stop-color="#e2e2e2"/>
      </linearGradient>
      <linearGradient id="aerial" x1="0" y1="0" x2="0" y2="1">
        <stop offset="0" stop-color="#8fa6c4"/><stop offset=".35" stop-color="#c9c3bd"/>
        <stop offset=".5" stop-color="#6d7690"/><stop offset=".7" stop-color="#b6b3ad"/>
        <stop offset=".85" stop-color="#d9d9d6"/><stop offset="1" stop-color="#3f7a3a"/>
      </linearGradient>
      <linearGradient id="p1" x1="0" y1="0" x2="0" y2="1"><stop offset="0" stop-color="#b9c8de"/><stop offset="1" stop-color="#3b3f46"/></linearGradient>
      <linearGradient id="p2" x1="0" y1="0" x2="0" y2="1"><stop offset="0" stop-color="#6f9bd6"/><stop offset="1" stop-color="#5d8c78"/></linearGradient>
      <linearGradient id="p3" x1="0" y1="0" x2="0" y2="1"><stop offset="0" stop-color="#7fa9e0"/><stop offset=".5" stop-color="#b79e7f"/><stop offset="1" stop-color="#ececec"/></linearGradient>
    </defs>
    <rect width="694" height="416" fill="url(#bgPaper)" role="img" aria-label="Faint white roof panel texture background"/>
    <polygon points="517,103 694,203 694,416 0,416 0,395" fill="url(#aerial)" role="img" aria-label="Aerial photo of a commercial district with mountains and farm fields"/>
    <polyline points="0,392 517,100 694,200" fill="none" stroke="#161a22" stroke-width="2"/>
    <polygon points="22,257 326,92 326,197 22,367" fill="#e85a1e"/>
    <polygon points="29,264 124,212 124,317 29,360" fill="url(#p1)" role="img" aria-label="Photo of a restaurant building exterior"/>
    <polygon points="130,209 222,159 222,266 130,314" fill="url(#p2)" role="img" aria-label="Photo of a metal roof with restaurant signage"/>
    <polygon points="228,155 319,106 319,193 228,262" fill="url(#p3)" role="img" aria-label="Photo of a flat white commercial rooftop"/>
  </svg>

  <div class="abs contact">
    <div class="contact-icons">
      <span><svg width="10" height="10" viewBox="0 0 24 24"><path d="M6.6 10.8a15 15 0 0 0 6.6 6.6l2.2-2.2a1 1 0 0 1 1-.25 11.4 11.4 0 0 0 3.6.6 1 1 0 0 1 1 1V20a1 1 0 0 1-1 1A17 17 0 0 1 3 4a1 1 0 0 1 1-1h3.5a1 1 0 0 1 1 1c0 1.25.2 2.45.6 3.6a1 1 0 0 1-.25 1z" fill="#e85a1e"/></svg></span>
      <span><svg width="11" height="11" viewBox="0 0 24 24"><circle cx="12" cy="12" r="10" fill="#e85a1e"/><path d="M2 12h20M12 2c3 3 3 17 0 20M12 2c-3 3-3 17 0 20" stroke="#fff" stroke-width="1.4" fill="none"/></svg></span>
      <span><svg width="10" height="11" viewBox="0 0 24 24"><path d="M12 2a7 7 0 0 0-7 7c0 5 7 13 7 13s7-8 7-13a7 7 0 0 0-7-7z" fill="#e85a1e"/><circle cx="12" cy="9" r="2.6" fill="#fff"/></svg></span>
    </div>
    <div class="phone">555-014-2290</div>
    <div class="web">www.summitcrest-roofing.com</div>
    <div class="address">4180 W Desert Ln<br>Peoria AZ 85345</div>
    <div class="rule"></div>
  </div>

  <div class="abs brand-top"><div class="l1">SUMMITCREST</div><div class="l2">ROOFING</div></div>

  <div class="abs band">
    <div class="abs brand-band"><div class="l1">SUMMITCREST</div><div class="l2">ROOFING</div></div>
    <div class="abs roc"><span class="orange">AZ ROC</span> 512760</div>
    <div class="abs tagline">COMMERCIAL SPECIALISTS<br>SINCE <span class="orange">1984</span></div>
    <div class="abs web-bar">www.summitcrest-roofing.com</div>
  </div>
</section>

<section class="page back">
  <svg class="art" width="694" height="535" viewBox="0 0 694 535">
    <defs>
      <linearGradient id="shop" x1="0" y1="0" x2="0" y2="1"><stop offset="0" stop-color="#8fb1dc"/><stop offset=".55" stop-color="#6b6459"/><stop offset="1" stop-color="#c9c9c6"/></linearGradient>
      <linearGradient id="roof" x1="0" y1="0" x2="0" y2="1"><stop offset="0" stop-color="#9fb0c4"/><stop offset=".3" stop-color="#c9cbcc"/><stop offset="1" stop-color="#e3e3e3"/></linearGradient>
    </defs>
    <polygon points="0,0 334,0 0,180" fill="url(#shop)" role="img" aria-label="Photo of a newly built coffee shop with a finished roof"/>
    <line x1="0" y1="180" x2="334" y2="0" stroke="#fff" stroke-width="1.5"/>
    <polygon points="370,0 694,0 694,185" fill="url(#roof)" role="img" aria-label="Photo of a white flat roof with rooftop vents"/>
    <line x1="370" y1="0" x2="694" y2="185" stroke="#fff" stroke-width="1.5"/>
  </svg>

  <div class="abs about">
    <div class="h2"><span class="orange">ABOUT</span> US</div>
    <div class="underline"></div>
    <p>Summitcrest Roofing opened the doors in 1984,<br>and we've since installed, serviced, maintained, and<br>coated thousands of commercial roofs around the state<br>of Arizona, in the many climate regions of the state.</p>
    <p>Though we all live here for the constant sunshine, Arizona is one of the<br>harshest environments in the US for roofs. Constant sun, heat, dryness,<br>and then the torrential monsoon downpours all test the limits of your roof.</p>
    <p>We work with you to come up with a solution that works for your roof and<br>will keep your business dry for years to come. Then, our team of project<br>managers, superintendents, foremen, and field workers all come<br>together to execute on that plan and install a quality roof.</p>
    <p>We are certified with many different manufacturers, so we're able to offer<br>custom solutions to solve your issues, that will also often come with<br>reputable manufacturer warranties.</p>
  </div>

  <div class="abs services-title">
    <div class="h2"><span class="orange">SERVICES</span> WE OFFER</div>
    <div class="underline"></div>
  </div>

  <div class="abs service" style="left:10px;top:386px">
    <div class="ico"><svg width="16" height="16" viewBox="0 0 24 24" fill="none" stroke="#e85a1e" stroke-width="1.6"><path d="M4 20 14 10M14 10l3-6 3 3-6 3M4 4l16 16M4 4l3 0 0 3"/></svg></div>
    <span class="orange">NEW ROOF</span><br>INSTALLATION
  </div>
  <div class="abs service" style="left:113px;top:386px">
    <div class="ico"><svg width="16" height="14" viewBox="0 0 24 20" fill="none" stroke="#e85a1e" stroke-width="1.6"><path d="M2 8 12 2l10 6M3 10h18M3 14h18M3 18h18M7 8v10M12 8v10M17 8v10"/></svg></div>
    <span class="orange">RE-</span>ROOFING
  </div>
  <div class="abs service" style="left:216px;top:386px">
    <div class="ico"><svg width="16" height="16" viewBox="0 0 24 24" fill="none" stroke="#e85a1e" stroke-width="1.6"><circle cx="12" cy="12" r="4"/><path d="M12 2v4M12 18v4M2 12h4M18 12h4M5 5l3 3M16 16l3 3M5 19l3-3M16 8l3-3"/></svg></div>
    <span class="orange">ROOF MAINTENANCE</span><br>AND SERVICE
  </div>
  <div class="abs service" style="left:10px;top:457px">
    <div class="ico"><svg width="16" height="16" viewBox="0 0 24 24" fill="none" stroke="#e85a1e" stroke-width="1.6"><circle cx="10" cy="10" r="6"/><path d="M14.5 14.5 21 21M7 10a3 3 0 0 1 6 0"/></svg></div>
    <span class="orange">ROOF</span><br>INSPECTIONS
  </div>
  <div class="abs service" style="left:113px;top:457px">
    <div class="ico"><svg width="16" height="16" viewBox="0 0 24 24" fill="none" stroke="#e85a1e" stroke-width="1.6"><rect x="4" y="3" width="14" height="6" rx="1"/><path d="M18 6h2v5h-9v3M10 14h2v7h-2z"/></svg></div>
    <span class="orange">ROOF</span><br>COATINGS
  </div>
  <div class="abs service" style="left:216px;top:457px">
    <div class="ico"><svg width="16" height="16" viewBox="0 0 24 24" fill="none" stroke="#e85a1e" stroke-width="1.6"><rect x="3" y="3" width="7" height="7" rx="2"/><rect x="14" y="3" width="7" height="7" rx="2"/><rect x="3" y="14" width="7" height="7" rx="2"/><path d="M17.5 14v7M14 17.5h7"/></svg></div>
    <span class="orange">AND</span><br>MORE...
  </div>

  <div class="abs install">
    <div class="h2"><span class="orange">WE INSTALL</span><br>THE FOLLOWING<br>PRODUCTS</div>
    <div class="underline"></div>
  </div>
  <div class="abs products">
    TPO<span class="sep"></span>PVC<span class="sep"></span>MODIFIED BITUMEN<span class="sep"></span>SILICONE COATINGS<br>
    ACRYLIC COATINGS<span class="sep"></span>SHINGLE<span class="sep"></span>METAL<span class="sep"></span>TILE<br>
    SPRAY POLYURETHANE FOAM<span class="sep"></span>AND MORE...
  </div>

  <div class="abs certified">
    <div class="h2"><span class="orange">CERTIFIED WITH THE</span><br>FOLLOWING MANUFACTURERS</div>
    <div class="underline"></div>
  </div>

  <div class="badge" style="left:367px;top:310px" role="img" aria-label="Manufacturer certification badge"><i></i></div>
  <div class="badge" style="left:444px;top:310px" role="img" aria-label="Manufacturer certification badge"><i></i></div>
  <div class="badge" style="left:520px;top:310px" role="img" aria-label="Manufacturer certification badge"><i></i></div>
  <div class="badge" style="left:597px;top:310px" role="img" aria-label="Manufacturer certification badge"><i></i></div>
  <div class="badge" style="left:405px;top:385px" role="img" aria-label="Manufacturer certification badge"><i></i></div>
  <div class="badge" style="left:482px;top:385px" role="img" aria-label="Manufacturer certification badge"><i></i></div>
  <div class="badge" style="left:558px;top:385px" role="img" aria-label="Manufacturer certification badge"><i></i></div>

  <div class="abs more"><span class="orange">AND MANY</span> MORE...</div>
  <div class="abs serving"><div class="a">SERVING</div><div class="b">THE ENTIRE STATE OF ARIZONA SINCE 1984</div></div>
</section>

</body>
</html>
```